New Webpage for High Class Expert Witness Services Company

We are looking for a minimalist design for a webpage that just has our logo and an entry form offer to connect with one of our Liaisons.
The entry form should just ask for Name, Email, Contact Info and Description of Project.

Company Name is: The Marlow Crest Advisory Services

Number of Pages Required

1 page

```html
<!DOCTYPE html>
<html lang="en">
<head>
<meta charset="utf-8">
<title>Marlow Crest Advisory Services — Connect with a Liaison</title>
<link href="https://fonts.googleapis.com/css2?family=Cormorant+Garamond:ital,wght@0,400;0,500;1,400&family=Inter:wght@400;500&family=JetBrains+Mono:wght@400;500&display=swap" rel="stylesheet">
<style>
  :root {
    --ink: #0b0b0b;
    --panel-dark: #0d0d0d;
    --logo-box: #141414;
    --paper: #f4f2ee;
    --white: #f2f0ec;
    --muted-light: #a8a8a8;
    --muted-dim: #6f6f6f;
    --accent-silver: #9aa0a6;
    --text-dark: #111111;
    --text-mid: #555555;
    --placeholder: #a3a3a3;
    --rule: #c9c6c0;
  }
  * { margin: 0; padding: 0; box-sizing: border-box; }
  html, body { width: 1200px; height: 639px; overflow: hidden; }
  body { position: relative; background: var(--paper); font-family: "Inter", sans-serif; }

  .intro-panel {
    position: absolute; left: 0; top: 0; width: 600px; height: 639px;
    background: linear-gradient(160deg, #131313 0%, var(--panel-dark) 50%, #101010 100%);
    color: var(--white);
  }
  .brand-box {
    position: absolute; left: 37px; top: 27px; width: 336px; height: 160px;
    background: var(--logo-box);
    display: flex; align-items: center; justify-content: center; gap: 10px;
  }
  .brand-mark { width: 12px; height: 12px; background: #bdbdbd; }
  .brand-name {
    font-family: "Cormorant Garamond", serif; font-weight: 500; font-size: 17px;
    letter-spacing: 0.06em; color: #d6d6d6; text-transform: uppercase;
  }
  .backdrop-glow {
    position: absolute; left: 130px; top: 185px; width: 340px; height: 305px;
    background: radial-gradient(ellipse at center, rgba(255,255,255,0.05) 0%, rgba(255,255,255,0.02) 45%, rgba(255,255,255,0) 70%);
  }
  .eyebrow {
    position: absolute; left: 37px; top: 285px; display: flex; align-items: center; gap: 8px;
    font-family: "JetBrains Mono", monospace; font-size: 7.5px; letter-spacing: 0.3em; color: var(--muted-light);
  }
  .eyebrow::before { content: ""; width: 19px; height: 1px; background: var(--muted-dim); }
  .intro-title {
    position: absolute; left: 37px; top: 312px;
    font-family: "Cormorant Garamond", serif; font-weight: 400; font-size: 47px; line-height: 49px;
    letter-spacing: -0.005em;
  }
  .intro-title em { color: var(--accent-silver); font-style: italic; }
  .intro-copy {
    position: absolute; left: 37px; top: 431px; width: 300px;
    font-size: 9.6px; line-height: 16.5px; color: var(--muted-light);
  }
  .meta { position: absolute; top: 590px; font-family: "JetBrains Mono", monospace; }
  .meta-label { font-size: 6.5px; letter-spacing: 0.2em; color: var(--muted-dim); }
  .meta-value { margin-top: 5px; font-size: 7.5px; letter-spacing: 0.12em; color: var(--white); }
  .meta-direct { left: 37px; }
  .meta-response { right: 37px; text-align: right; }

  .form-panel { position: absolute; left: 600px; top: 0; width: 600px; height: 639px; background: var(--paper); }
  .form-title {
    position: absolute; left: 37px; top: 155px;
    font-family: "Cormorant Garamond", serif; font-weight: 400; font-size: 29px; color: var(--text-dark);
  }
  .form-lede { position: absolute; left: 37px; top: 196px; font-size: 9.3px; color: var(--text-mid); }
  .field { position: absolute; }
  .field label {
    display: block; font-family: "JetBrains Mono", monospace; font-size: 7px;
    letter-spacing: 0.25em; color: #555;
  }
  .field input, .field textarea {
    display: block; width: 100%; margin-top: 8px; border: 0; border-bottom: 1px solid var(--rule);
    background: transparent; font-family: "Inter", sans-serif; font-size: 9.8px; color: var(--text-dark);
    padding: 4px 0 7px; outline: none; resize: none;
  }
  .field input::placeholder, .field textarea::placeholder { color: var(--placeholder); }
  .field-name { left: 37px; top: 236px; width: 347px; }
  .field-email { left: 37px; top: 291px; width: 164px; }
  .field-contact { left: 220px; top: 291px; width: 164px; }
  .field-desc { left: 37px; top: 351px; width: 347px; }
  .field-desc textarea { height: 64px; padding-top: 6px; }
  .submit {
    position: absolute; left: 37px; top: 442px; width: 145px; height: 32px;
    background: var(--ink); color: #fff; border: 0; display: flex; align-items: center; justify-content: center; gap: 10px;
    font-family: "Inter", sans-serif; font-weight: 500; font-size: 8.8px; letter-spacing: 0.1em;
  }
  .consent { position: absolute; left: 198px; top: 447px; width: 190px; font-size: 7.4px; line-height: 11px; color: var(--text-mid); }
  .site-footer {
    position: absolute; left: 37px; right: 38px; top: 603px; display: flex; justify-content: space-between;
    font-family: "JetBrains Mono", monospace; font-size: 7.5px; letter-spacing: 0.15em; color: #555;
  }
  .site-footer nav { display: flex; gap: 19px; }
  .site-footer a { color: inherit; text-decoration: none; }
</style>
</head>
<body>
  <section class="intro-panel">
    <div class="brand-box">
      <span class="brand-mark"></span>
      <span class="brand-name">The Marlow Crest Advisory Services</span>
    </div>
    <div class="backdrop-glow" role="img" aria-label="Faint geometric circle motif behind the heading"></div>
    <p class="eyebrow">LIAISON INTAKE · CONFIDENTIAL</p>
    <h1 class="intro-title">Request a <em>private</em><br>consultation.</h1>
    <p class="intro-copy">Tell us about your matter. A dedicated liaison will review your request and respond within one business day to coordinate medical expert integration.</p>
    <div class="meta meta-direct">
      <p class="meta-label">DIRECT</p>
      <p class="meta-value">INTAKE@MARLOWCREST.ADVISORY</p>
    </div>
    <div class="meta meta-response">
      <p class="meta-label">RESPONSE</p>
      <p class="meta-value">&lt; 24 HOURS</p>
    </div>
  </section>

  <section class="form-panel">
    <h2 class="form-title">Connect with a Liaison</h2>
    <p class="form-lede">All submissions are reviewed under attorney-client privilege where applicable.</p>
    <form>
      <div class="field field-name"><label for="name">NAME *</label><input id="name" type="text" placeholder="Full name"></div>
      <div class="field field-email"><label for="email">EMAIL *</label><input id="email" type="email" placeholder="you@firm.com"></div>
      <div class="field field-contact"><label for="contact">CONTACT INFO *</label><input id="contact" type="text" placeholder="Phone or preferred method"></div>
      <div class="field field-desc"><label for="desc">DESCRIPTION OF PROJECT *</label><textarea id="desc" placeholder="Case type, jurisdiction, timeline, and any specific expertise needed..."></textarea></div>
      <button class="submit" type="submit">SUBMIT REQUEST
        <svg width="13" height="8" viewBox="0 0 13 8" fill="none" stroke="#fff" stroke-width="1"><path d="M0 4h12M8.5 0.5L12 4l-3.5 3.5"/></svg>
      </button>
      <p class="consent">By submitting, you agree to our confidentiality and communication terms.</p>
    </form>
    <footer class="site-footer">
      <span>© 2026 MARLOW CREST</span>
      <nav><a href="#">PRIVACY</a><a href="#">TERMS</a><a href="#">COMPLIANCE</a></nav>
    </footer>
  </section>
</body>
</html>
```